Interior Stylist business card design needed

I need a business card for my new company in Sydney called "Lu Brannigan Designs". The business offers an interior styling and colour consultancy. My clients are generally not very design savvy (hence why they use me) and can range from being quite conservative to really wanting something "out there". They can be looking for a budget makeover or something more expensive / substantial. I'd like my business card design to be stylish (but not overly formal). I certainly don't want it to be conservative. I'd like it to stand out a bit! I don't really have any aversion to particular colours and I don't have a logo as such - my business name is really all I have.

Target Market(s)

As above - home owners, ranging from conservative to modern

Industry/Entity Type

Conservative

Contact Information for Business Card

Lu Brannigan Designs
Colour consultancy and interior styling
ph: 0417 368 205
email: lubrannigan@zephmail.net.au

Requirements
Should not have
• Old fashioned writing or motifs. No Times Roman font!!

```html
<!DOCTYPE html>
<html lang="en">
<head>
<meta charset="utf-8">
<title>Lu Brannigan Designs – Business Card</title>
<link rel="stylesheet" href="https://fonts.googleapis.com/css2?family=Jost:wght@400;600&display=swap">
<style>
  :root {
    --card-red: #d9251d;
    --ink-dark: #231f20;
    --ink-light: #ffffff;
    --accent-yellow: #fff200;
    --accent-blue: #7ac6f1;
    --accent-green: #86c12a;
  }
  html, body {
    margin: 0;
    padding: 0;
    width: 1200px;
    height: 686px;
    overflow: hidden;
    background: var(--card-red);
  }
  .business-card {
    position: relative;
    width: 1200px;
    height: 686px;
    background: var(--card-red);
    overflow: hidden;
    font-family: "Jost", "Century Gothic", sans-serif;
  }
  .business-name {
    position: absolute;
    left: 0;
    top: 82px;
    width: 1200px;
    margin: 0;
    text-align: center;
    font-weight: 600;
    font-size: 112px;
    line-height: 1;
    letter-spacing: 2px;
    color: var(--ink-dark);
    white-space: nowrap;
  }
  .tagline {
    position: absolute;
    left: 0;
    top: 348px;
    width: 1200px;
    margin: 0;
    text-align: center;
    font-weight: 400;
    font-size: 64px;
    line-height: 1;
    letter-spacing: 1.5px;
    color: var(--ink-dark);
    white-space: nowrap;
  }
  .colour-accent {
    position: absolute;
    left: 0;
    bottom: 0;
    width: 190px;
    height: 200px;
    background: linear-gradient(160deg, var(--accent-green) 0%, var(--accent-blue) 50%, var(--accent-yellow) 100%);
  }
  .contact-details {
    position: absolute;
    left: 0;
    top: 548px;
    width: 1200px;
    margin: 0;
    text-align: center;
    font-style: normal;
    font-weight: 400;
    font-size: 40px;
    line-height: 50px;
    letter-spacing: 0.5px;
    color: var(--ink-light);
  }
  .contact-line {
    display: block;
    white-space: nowrap;
  }
</style>
</head>
<body>
  <main class="business-card">
    <div class="colour-accent" role="img" aria-label="Colour accent block in yellow, blue and green"></div>

    <h1 class="business-name">Lu Brannigan Designs</h1>
    <p class="tagline">Colour consultancy and interior styling</p>

    <address class="contact-details">
      <span class="contact-line">Telephone: (417)&nbsp; 368-205</span>
      <span class="contact-line">Email: lubrannigan@zephmail.net.au</span>
    </address>
  </main>
</body>
</html>
```